Auto electrical business that is mobile so we come to you so it doesn't matter if the car, 4wd, cara

We need a business card designed that will capture people's attention. We are based in Bathurst & we are a Mobile Auto Electrical business that works on cars, 4dw's, caravans, trucks, farming equipment through to mining equipment

```html
<!DOCTYPE html>
<html lang="en">
<head>
<meta charset="utf-8">
<title>Reno's Mobile Auto Electrical – Business Card</title>
<link rel="stylesheet" href="https://fonts.googleapis.com/css2?family=Montserrat:wght@500;600;700;800&family=Russo+One&display=swap">
<style>
  :root{
    --stage:#2b2f36;
    --card-black:#050505;
    --navy:#0c1a45;
    --navy-deep:#060d28;
    --yellow:#f7d117;
    --orange:#f39a1b;
    --red:#e8351e;
    --silver:#cfd3d8;
    --silver-dark:#7d838b;
    --white:#f4f4f4;
    --grey-text:#c9c9c9;
  }
  *{margin:0;padding:0;box-sizing:border-box}
  html,body{width:1200px;height:900px;overflow:hidden;background:var(--stage)}
  body{font-family:"Montserrat",sans-serif;position:relative}

  .card{position:absolute;width:540px;height:310px;border-radius:6px;overflow:hidden;box-shadow:0 12px 30px rgba(0,0,0,.45)}
  .card--front{left:40px;top:295px;background:var(--card-black)}
  .card--back{left:620px;top:295px;background:radial-gradient(ellipse at 60% 40%,#1d2f72 0%,var(--navy) 45%,var(--navy-deep) 100%)}

  /* front */
  .brand-mark{position:absolute;left:26px;top:22px;display:flex;align-items:center;gap:10px}
  .brand-mark__dot{width:18px;height:18px;border-radius:50%;background:var(--yellow)}
  .brand-mark__name{font-weight:800;font-size:22px;color:var(--yellow);letter-spacing:1px}

  .contact{position:absolute;left:26px;top:78px;list-style:none}
  .contact__item{display:flex;align-items:center;gap:8px;font-size:12px;color:var(--white);line-height:19px}
  .contact__item--main{color:var(--yellow);font-weight:700;font-size:15px}
  .contact__icon{width:12px;height:12px;flex:none}
  .contact__rule{position:absolute;left:26px;top:146px;width:150px;height:1px;background:var(--grey-text)}
  .licences{position:absolute;left:26px;top:154px;font-size:10px;color:var(--grey-text);line-height:14px}

  .silver-bar{position:absolute;left:250px;top:20px;width:290px;height:14px;border-radius:7px 0 0 7px;background:linear-gradient(180deg,#eef0f2,var(--silver-dark))}
  .wordmark{position:absolute;left:240px;top:40px;font-family:"Russo One",sans-serif;font-size:62px;line-height:1;color:var(--silver);letter-spacing:1px}
  .tagline{position:absolute;left:240px;top:110px;font-weight:800;font-size:16px;color:var(--orange);letter-spacing:.3px}

  .wires{position:absolute;left:0;top:196px;width:270px;height:72px;opacity:.85;
    background:linear-gradient(100deg,#050505 0%,#3a2a4a 30%,#2b4fa8 55%,#c8452a 75%,#050505 100%)}

  .services{position:absolute;right:22px;bottom:16px;list-style:none;text-align:right;font-weight:700;font-size:11px;line-height:15px;text-transform:uppercase}
  .services li:nth-child(1){color:var(--red)}
  .services li:nth-child(2){color:var(--red)}
  .services li:nth-child(3){color:var(--orange)}
  .services li:nth-child(4){color:var(--yellow)}

  /* back */
  .panels{position:absolute;left:0;top:0;width:540px;height:310px}
  .back-phone{position:absolute;left:26px;top:248px;font-weight:800;font-size:24px;color:var(--yellow);letter-spacing:2px}
</style>
</head>
<body>

<section class="card card--front" aria-label="Business card front">
  <div class="brand-mark">
    <span class="brand-mark__dot"></span>
    <span class="brand-mark__name">RENO'S</span>
  </div>

  <ul class="contact">
    <li class="contact__item contact__item--main">
      <svg class="contact__icon" viewBox="0 0 12 12"><circle cx="6" cy="6" r="6" fill="#f39a1b"/><path d="M3.5 3.2l1.4-.4.8 1.6-.8.6a4 4 0 0 0 1.9 1.9l.6-.8 1.6.8-.4 1.4c-2.8.2-5.3-2.3-5.1-5.1z" fill="#050505"/></svg>
      048800SPARK
    </li>
    <li class="contact__item">
      <svg class="contact__icon" viewBox="0 0 12 12"><circle cx="6" cy="6" r="6" fill="#f39a1b"/><path d="M3.5 3.2l1.4-.4.8 1.6-.8.6a4 4 0 0 0 1.9 1.9l.6-.8 1.6.8-.4 1.4c-2.8.2-5.3-2.3-5.1-5.1z" fill="#050505"/></svg>
      0488112233
    </li>
    <li class="contact__item">
      <svg class="contact__icon" viewBox="0 0 12 12"><circle cx="6" cy="6" r="6" fill="#e8351e"/><rect x="3" y="4" width="6" height="4.2" fill="none" stroke="#050505" stroke-width=".9"/><path d="M3 4l3 2.3L9 4" fill="none" stroke="#050505" stroke-width=".9"/></svg>
      renosmobile@mailbox.com
    </li>
  </ul>
  <div class="contact__rule"></div>
  <p class="licences">MVRL10293<br>AU20194</p>

  <div class="silver-bar"></div>
  <h1 class="wordmark">RENO'S</h1>
  <p class="tagline">MOBILE AUTO ELECTRICAL</p>

  <div class="wires" role="img" aria-label="Photo of stripped multicoloured electrical wires with sparks arcing between them"></div>

  <ul class="services">
    <li>All farming and plant equipment</li>
    <li>Air-con needs</li>
    <li>Light and heavy vehicle</li>
    <li>Caravan and camping systems</li>
  </ul>
</section>

<section class="card card--back" aria-label="Business card back">
  <svg class="panels" viewBox="0 0 540 310">
    <polygon points="30,30 190,30 140,230 30,230" fill="#7a6a3a" role="img" aria-label="Photo of a green combine harvester in a wheat field at dusk"/>
    <polygon points="190,30 390,30 340,230 140,230" fill="#8f9a8a" role="img" aria-label="Photo of a white ute with a camper trailer set up under trees"/>
    <polygon points="390,30 540,30 540,230 340,230" fill="#2a3550" role="img" aria-label="Close-up photo of a car headlight glowing at night"/>
    <g fill="none" stroke="#f7d117" stroke-width="3">
      <line x1="30" y1="30" x2="540" y2="30"/>
      <line x1="30" y1="230" x2="540" y2="230"/>
      <line x1="30" y1="30" x2="30" y2="230"/>
      <line x1="190" y1="30" x2="140" y2="230"/>
      <line x1="390" y1="30" x2="340" y2="230"/>
    </g>
  </svg>
  <p class="back-phone">PHONE: 048800SPARK</p>
</section>

</body>
</html>
```